Travel Vaccination Service Flyer

Elmbrook Pharmacy has been providing services to the local community for 40 years. To mark this miestone, we are launching a travel vaccination clinic. We aim to distribute flyers to homes and businesses in the surrounding area in January 2014.
Example files for reference are attached for travel and Pharmacy service
Front Side - background images relating to Pharmacy and Health
"Elmbrook Pharmacy Travel Vaccination Clinic"
47 Elmbrook Road
London, SE9 7QJ
Our Logo (attached file)
Images depicting Holidays, travel, beach & Trek below our Logo
Vaccination names:
Hepatitis (A & B),
Japanese Encephalitis,
Typhoid,
Cholera,
Diptheria, Tetanus &Polio,
Tick Born Encephalitis
Appointments and walk-ins available
Call our travel clinic on ...XXXXXXX...... to book an appointment
The bottom of the flyer should have a voucher:
5% off final vaccination bill upon production of this leaflet
Reverse Side
Logo (attached file)
47 Elmbrook Road
London, SE9 7QJ
Services available:
Repeat Prescription collection and delivery service
Stop Smoking Clinic
Emergency Contraception
Contraceptive Pill
PHB Pharmacy Direct Minor ailments service
Contact out Pharmacy team on: 02079460518
E: info@elmbrookpharmacy.co.uk

```html
<!DOCTYPE html>
<html lang="en">
<head>
<meta charset="utf-8">
<title>Elmbrook Pharmacy – Travel Vaccination Clinic Flyer</title>
<link href="https://fonts.googleapis.com/css2?family=Roboto:wght@300;400;700;900&family=Roboto+Condensed:wght@400;700&display=swap" rel="stylesheet">
<style>
  :root {
    --backdrop: #8a8a8a;
    --paper: #ffffff;
    --green: #2bb15f;
    --blue: #05aeec;
    --yellow: #fff200;
    --ink: #222222;
    --grey-text: #555555;
    --logo-blue: #1f8fd6;
  }
  * { box-sizing: border-box; margin: 0; padding: 0; }
  html, body { width: 1200px; height: 857px; overflow: hidden; }
  body {
    position: relative;
    background: var(--backdrop);
    font-family: "Roboto", Arial, sans-serif;
    color: var(--ink);
  }
  .sheet {
    position: absolute;
    top: 68px;
    width: 508px;
    height: 720px;
    background: var(--paper);
  }
  .sheet--front { left: 55px; }
  .sheet--back { left: 632px; }
  .abs { position: absolute; }

  /* Front */
  .front-brand {
    left: 25px; top: 44px;
    font-weight: 300; font-size: 25px; letter-spacing: 0.3px;
    color: var(--ink);
  }
  .front-title {
    left: 24px; top: 80px;
    font-weight: 900; font-size: 40px; line-height: 39px;
    color: var(--green); letter-spacing: 0.5px;
  }
  .front-address {
    left: 28px; top: 222px;
    font-weight: 700; font-size: 13.5px;
  }
  .voucher {
    left: 333px; top: 26px; width: 154px; height: 114px;
    background: var(--blue); color: #fff;
    padding: 10px 15px;
    font-family: "Roboto Condensed", Arial, sans-serif;
  }
  .voucher__amount {
    font-weight: 700; font-size: 46px; line-height: 46px;
    color: var(--yellow);
  }
  .voucher__amount small { font-size: 36px; }
  .voucher__text { font-weight: 700; font-size: 14px; line-height: 17px; margin-top: 6px; }
  .vaccines {
    left: 333px; top: 152px; width: 154px; height: 261px;
    background: var(--green); color: #fff;
    padding: 8px 15px;
    font-family: "Roboto Condensed", Arial, sans-serif;
    font-weight: 700;
  }
  .vaccines__title { font-size: 18px; line-height: 20px; margin-bottom: 4px; }
  .vaccines__list { list-style: none; font-size: 14px; line-height: 22.8px; }
  .photo { position: absolute; }
  .photo--trek { left: 23px; top: 257px; width: 150px; height: 157px; background: linear-gradient(180deg, #4f8fd8 0%, #9fc7e8 45%, #5c7a54 75%, #4a4a44 100%); }
  .photo--family { left: 182px; top: 257px; width: 144px; height: 157px; background: linear-gradient(160deg, #3d7fd3 0%, #8fbfe8 40%, #a8683f 75%, #5a3a2a 100%); }
  .photo--beach { left: 23px; top: 422px; width: 150px; height: 148px; background: linear-gradient(180deg, #3c8fd6 0%, #b7dcf1 40%, #3fbfc6 60%, #e8dcc0 80%, #c79a5a 100%); }
  .photo--injection { left: 182px; top: 422px; width: 305px; height: 148px; background: linear-gradient(100deg, #d9dde0 0%, #eef0f1 45%, #d4a58a 70%, #8a5fa6 100%); }
  .appointments {
    left: 23px; top: 588px;
    font-weight: 400; font-size: 16px; line-height: 22px; color: var(--ink);
  }
  .phone {
    left: 21px; top: 634px;
    display: flex; align-items: center; gap: 3px;
    font-family: "Roboto Condensed", Arial, sans-serif;
    font-weight: 700; font-size: 27px; color: var(--green);
  }
  .logo {
    display: flex; align-items: center; gap: 8px;
    font-family: "Roboto Condensed", Arial, sans-serif;
    font-weight: 400; color: var(--logo-blue);
  }
  .logo__dot { width: 20px; height: 20px; border-radius: 50%; background: var(--green); flex: none; }
  .logo--front { left: 250px; top: 607px; font-size: 27px; }
  .band {
    left: 23px; top: 673px; width: 464px; height: 22px;
    background: var(--green); color: #fff;
    font-weight: 700; font-size: 16.5px; line-height: 22px; text-align: center;
  }

  /* Back */
  .photo--team { left: 20px; top: 17px; width: 468px; height: 253px; background: linear-gradient(90deg, #ffffff 0%, #8fc4e4 25%, #b7d9ee 50%, #e8eef2 75%, #ffffff 100%); }
  .services {
    left: 20px; top: 283px; width: 468px; height: 179px;
    background: var(--green); color: #fff;
  }
  .photo--pills {
    left: 24px; top: 15px; width: 146px; height: 148px;
    border: 4px solid #fff;
    background: linear-gradient(135deg, #e9eef2 0%, #c9d6de 45%, #d4a48a 75%, #9fb7c8 100%);
  }
  .services__body {
    left: 192px; top: 14px;
    font-family: "Roboto Condensed", Arial, sans-serif; font-weight: 700;
  }
  .services__title { font-size: 17px; margin-bottom: 4px; }
  .services__list { list-style: none; font-size: 14px; line-height: 17px; }
  .services__list li { display: flex; gap: 6px; margin-bottom: 5.5px; }
  .services__list svg { flex: none; margin-top: 2px; }
  .contact {
    left: 20px; top: 462px; width: 468px; height: 56px;
    background: var(--blue); color: #fff;
    padding: 6px 27px;
    font-family: "Roboto Condensed", Arial, sans-serif; font-weight: 700;
    font-size: 16px; line-height: 22px;
  }
  .logo--back { left: 40px; top: 569px; font-size: 31px; }
  .back-address {
    left: 47px; top: 640px;
    font-weight: 700; font-size: 13px; color: var(--grey-text);
  }
  .map { left: 312px; top: 529px; width: 174px; height: 141px; background: linear-gradient(135deg, #e4f1dc 0%, #d6e9cc 50%, #eef5e8 100%); border: 1px solid #aaa; }
  .band--back { left: 20px; top: 677px; width: 468px; height: 24px; font-size: 17px; line-height: 24px; }
</style>
</head>
<body>
  <section class="sheet sheet--front">
    <p class="abs front-brand">ELMBROOK PHARMACY</p>
    <h1 class="abs front-title">TRAVEL<br>VACCINATION<br>CLINIC</h1>
    <p class="abs front-address">47 Elmbrook Road, London, SE9 7QJ</p>

    <div class="abs voucher">
      <p class="voucher__amount">5% <small>off</small></p>
      <p class="voucher__text">final vaccination bill with this leaflet</p>
    </div>

    <div class="abs vaccines">
      <h2 class="vaccines__title">VACCINATION<br>NAMES:</h2>
      <ul class="vaccines__list">
        <li>Hepatitis (A &amp; B)</li>
        <li>Japanese Encephalitis</li>
        <li>Typhoid</li>
        <li>Cholera</li>
        <li>Diptheria</li>
        <li>Tetanus &amp;Polio</li>
        <li>Tick Borne Encephalitis</li>
        <li>Meningitis ACWY</li>
        <li>MMR</li>
      </ul>
    </div>

    <div class="photo photo--trek" role="img" aria-label="Hikers on a mountain summit overlooking a valley"></div>
    <div class="photo photo--family" role="img" aria-label="Happy family smiling together outdoors"></div>
    <div class="photo photo--beach" role="img" aria-label="Couple relaxing in deck chairs on a tropical beach"></div>
    <div class="photo photo--injection" role="img" aria-label="Gloved hand giving a vaccination injection in an arm"></div>

    <p class="abs appointments">Appointments and<br>walk-ins available</p>
    <p class="abs phone">
      <svg width="10" height="22" viewBox="0 0 10 22" aria-hidden="true"><path d="M8 1 C3 3 1 7 1 11 C1 15 3 19 8 21" fill="none" stroke="#2bb15f" stroke-width="3" stroke-linecap="round"/></svg>
      0207 946 0518
    </p>
    <div class="abs logo logo--front"><span class="logo__dot"></span>Elmbrook Pharmacy</div>
    <p class="abs band">Call our travel clinic to book an appointment</p>
  </section>

  <section class="sheet sheet--back">
    <div class="photo photo--team" role="img" aria-label="Team of smiling pharmacy and medical staff"></div>

    <div class="abs services">
      <div class="photo photo--pills" role="img" aria-label="Hands holding blister packs of tablets"></div>
      <div class="abs services__body">
        <h2 class="services__title">SERVICES AVAILABLE:</h2>
        <ul class="services__list">
          <li><svg width="12" height="12" viewBox="0 0 12 12" aria-hidden="true"><circle cx="6" cy="6" r="6" fill="#fff"/><path d="M3 6.2 L5.2 8.3 L9 4" fill="none" stroke="#05aeec" stroke-width="1.8"/></svg><span>Repeat Prescription collection<br>and delivery service</span></li>
          <li><svg width="12" height="12" viewBox="0 0 12 12" aria-hidden="true"><circle cx="6" cy="6" r="6" fill="#fff"/><path d="M3 6.2 L5.2 8.3 L9 4" fill="none" stroke="#05aeec" stroke-width="1.8"/></svg><span>Stop Smoking Clinic</span></li>
          <li><svg width="12" height="12" viewBox="0 0 12 12" aria-hidden="true"><circle cx="6" cy="6" r="6" fill="#fff"/><path d="M3 6.2 L5.2 8.3 L9 4" fill="none" stroke="#05aeec" stroke-width="1.8"/></svg><span>Emergency Contraception</span></li>
          <li><svg width="12" height="12" viewBox="0 0 12 12" aria-hidden="true"><circle cx="6" cy="6" r="6" fill="#fff"/><path d="M3 6.2 L5.2 8.3 L9 4" fill="none" stroke="#05aeec" stroke-width="1.8"/></svg><span>Contraceptive Pill</span></li>
          <li><svg width="12" height="12" viewBox="0 0 12 12" aria-hidden="true"><circle cx="6" cy="6" r="6" fill="#fff"/><path d="M3 6.2 L5.2 8.3 L9 4" fill="none" stroke="#05aeec" stroke-width="1.8"/></svg><span>PHB Pharmacy Direct Minor ailments service</span></li>
        </ul>
      </div>
    </div>

    <div class="abs contact">
      <p>Contact out Pharmacy team on: 02079460518</p>
      <p>E: info@elmbrookpharmacy.co.uk</p>
    </div>

    <div class="abs logo logo--back"><span class="logo__dot"></span>Elmbrook Pharmacy</div>
    <p class="abs back-address">47 Elmbrook Road,&nbsp; London, SE9 7QJ</p>
    <div class="abs map" role="img" aria-label="Street map showing how to find the pharmacy"></div>
    <p class="abs band band--back">Friendly staff, always very helpful and polite</p>
  </section>
</body>
</html>
```